Tall Heron Vodka

We are launching a new mainstream Vodka brand "Tall Heron" to take on big brands. China will be first market. The category norms seems to be Red and Black on a clear bottle and we would expect some red but does not need to be entirely red. The design would need to work on both clear (Valdorin) and frosted (Pale Finch) style bottles. In the future we will have gold heron, silver heron, platinum heron and diamond heron for more premium variants.

Target Market(s)

China

Industry/Entity Type

Alcohol

Colors
EB3D1F
EC4F4E
F09395
F8D3D4
FCEDEE

Requirements
Must have
• Space for Chinese language as well ad English
Nice to have
• Energetic, Engaging
Should not have
• Not stereotypes of photo of bad looking bear. Good looking bear, light not heavy.

```html
<!DOCTYPE html>
<html lang="en">
<head>
<meta charset="utf-8">
<title>Tall Heron Vodka – Label</title>
<link rel="stylesheet" href="https://fonts.googleapis.com/css2?family=Playfair+Display:wght@900&family=Cinzel:wght@400;600&family=Libre+Baskerville&family=Noto+Serif+SC:wght@600&display=swap">
<style>
  :root {
    --backdrop: #e6e6e8;
    --label-white: #ffffff;
    --brand-red: #e0231b;
    --band-black: #1c1a1a;
    --band-edge: #3a1f1c;
    --text-dark: #222222;
    --mist-light: #f1f2f4;
    --mist-grey: #d6d8dc;
    --claw-red: #c8202a;
  }
  html, body {
    margin: 0;
    padding: 0;
    width: 845px;
    height: 1200px;
    overflow: hidden;
    background: var(--backdrop);
  }
  .canvas {
    position: relative;
    width: 845px;
    height: 1200px;
    display: flex;
    align-items: center;
    justify-content: center;
  }
  .label {
    position: relative;
    width: 640px;
    height: 1000px;
    background: var(--label-white);
    box-sizing: border-box;
  }
  .brand-name {
    position: absolute;
    top: 92px;
    left: 0;
    right: 0;
    margin: 0;
    text-align: center;
    font-family: "Playfair Display", serif;
    font-weight: 900;
    font-size: 80px;
    letter-spacing: 1px;
    color: var(--brand-red);
    line-height: 1;
  }
  .brand-name-local {
    position: absolute;
    top: 192px;
    left: 0;
    right: 0;
    margin: 0;
    text-align: center;
    font-family: "Noto Serif SC", serif;
    font-weight: 600;
    font-size: 30px;
    letter-spacing: 14px;
    padding-left: 14px;
    line-height: 1;
    color: var(--text-dark);
  }
  .hero-art {
    position: absolute;
    top: 250px;
    left: 0;
    width: 640px;
    height: 420px;
    display: block;
  }
  .spirit-band {
    position: absolute;
    top: 690px;
    left: 0;
    right: 0;
    height: 96px;
    background: var(--band-black);
    border-top: 6px solid var(--band-edge);
    border-bottom: 6px solid var(--band-edge);
    display: flex;
    align-items: center;
    justify-content: center;
  }
  .spirit-name {
    margin: 0;
    font-family: "Cinzel", serif;
    font-weight: 400;
    font-size: 56px;
    letter-spacing: 28px;
    padding-left: 28px;
    color: var(--label-white);
  }
  .spirit-note {
    position: absolute;
    top: 815px;
    left: 0;
    right: 0;
    margin: 0;
    text-align: center;
    font-family: "Cinzel", serif;
    font-weight: 600;
    font-size: 24px;
    letter-spacing: 3px;
    color: var(--text-dark);
  }
  .spirit-note-local {
    position: absolute;
    top: 862px;
    left: 0;
    right: 0;
    margin: 0;
    text-align: center;
    font-family: "Noto Serif SC", serif;
    font-weight: 600;
    font-size: 20px;
    letter-spacing: 6px;
    padding-left: 6px;
    color: var(--text-dark);
  }
  .volume, .strength {
    position: absolute;
    bottom: 40px;
    margin: 0;
    font-family: "Libre Baskerville", serif;
    font-weight: 400;
    font-size: 18px;
    color: var(--text-dark);
  }
  .volume { left: 40px; }
  .strength { right: 40px; }
</style>
</head>
<body>
  <main class="canvas">
    <section class="label">
      <h1 class="brand-name">TALL HERON</h1>
      <p class="brand-name-local" lang="zh-Hans">高鹭伏特加</p>

      <svg class="hero-art" viewBox="0 0 640 420" role="img" aria-label="Illustration of red claw marks over pale misty mountain peaks">
        <defs>
          <linearGradient id="mist" x1="0" y1="0" x2="0" y2="1">
            <stop offset="0" stop-color="#f1f2f4"/>
            <stop offset="0.6" stop-color="#d6d8dc"/>
            <stop offset="1" stop-color="#f1f2f4"/>
          </linearGradient>
          <radialGradient id="claw-glow" cx="0.5" cy="0.45" r="0.35">
            <stop offset="0" stop-color="#c8202a" stop-opacity="0.55"/>
            <stop offset="1" stop-color="#c8202a" stop-opacity="0"/>
          </radialGradient>
        </defs>
        <rect width="640" height="420" fill="url(#mist)"/>
        <rect width="640" height="420" fill="url(#claw-glow)"/>
      </svg>

      <div class="spirit-band">
        <h2 class="spirit-name">VODKA</h2>
      </div>
      <p class="spirit-note">TRIPLE DISTILLED</p>
      <p class="spirit-note-local" lang="zh-Hans">三次蒸馏</p>

      <p class="volume">70cl</p>
      <p class="strength">37,5%Vol</p>
    </section>
  </main>
</body>
</html>
```